Money transfer app

I want a redesign of 3-4 screens of the mobile app.

I want:
1. Splash screen
2. Welcome screen
3. Login screen
4. More options. to send screen

I have attached existing designs.

```html
<!DOCTYPE html>
<html lang="en">
<head>
<meta charset="utf-8">
<title>Swift Send – App Screens</title>
<link href="https://fonts.googleapis.com/css2?family=Lexend:wght@300;400;500;600&display=swap" rel="stylesheet">
<style>
:root{
  --bg:#dbe9d4;
  --forest:#0f4a12;
  --forest-deep:#0b3a0d;
  --leaf:#2f9a2a;
  --lime:#86e55a;
  --mint:#f2fbec;
  --ink:#0d3a10;
  --text:#1b1b1b;
  --muted:#8a8a8a;
  --white:#ffffff;
}
*{box-sizing:border-box;margin:0;padding:0}
html,body{width:1200px;height:573px;overflow:hidden;background:var(--bg);font-family:"Lexend",sans-serif;color:var(--text)}
.canvas{position:relative;width:1200px;height:573px}
.screen{position:absolute;top:57px;width:237px;height:459px;border-radius:20px;overflow:hidden;background:var(--white)}
.screen--splash{left:54px;background:var(--forest)}
.screen--welcome{left:335px}
.screen--login{left:614px}
.screen--options{left:911px}
.abs{position:absolute}
.splash-pattern{position:absolute;inset:0;background:radial-gradient(circle at 50% 48%,#1d6a1f 0%,#13521a 45%,var(--forest) 80%)}
.splash-strip{position:absolute;left:0;right:0;bottom:0;height:8px;background:var(--lime)}
.brand{position:absolute;left:0;right:0;display:flex;align-items:center;justify-content:center;gap:7px;color:var(--white);font-weight:500}
.brand-dot{border-radius:50%;border:3px solid var(--lime)}
.brand--splash{top:214px;font-size:28px}
.brand--splash .brand-dot{width:30px;height:30px}
.brand--header{top:45px;font-size:23px}
.brand--header .brand-dot{width:24px;height:24px;border-width:2.5px}
.header{position:absolute;left:0;top:0;width:237px;height:130px}
.status{position:absolute;top:9px;left:12px;right:14px;display:flex;justify-content:space-between;align-items:center;color:var(--white);font-size:8.5px;font-weight:500}
.status small{font-size:5px}
.status-icons{display:flex;gap:5px;align-items:center}
.title{position:absolute;left:0;right:0;text-align:center;color:var(--ink);font-weight:600}
.welcome-title{top:140px;font-size:18.5px}
.welcome-sub{position:absolute;left:0;right:0;top:174px;text-align:center;font-size:10.5px;line-height:18px;font-weight:300;color:#111}
.welcome-note{position:absolute;left:20px;right:20px;top:219px;text-align:center;font-size:10.5px;line-height:18px;color:var(--leaf)}
.welcome-note .tick{display:inline-block;width:8px;height:8px;border-radius:50%;background:var(--leaf);vertical-align:0px;margin-right:4px}
.welcome-art{position:absolute;left:0;right:0;top:275px;height:160px;background:linear-gradient(180deg,#fbfcf6 0%,#f3f6e4 50%,#f2c9a8 100%)}
.login-title{top:136px;font-size:18px;line-height:23px}
.login-hello{position:absolute;left:0;right:0;top:196px;text-align:center;font-size:9px;font-weight:500;color:#111}
.field{position:absolute;left:11px;width:215px;height:31px;border:1px solid var(--lime);border-radius:5px;background:var(--mint);font-size:8.5px;color:#a8a8a8;font-weight:300;padding:9px 14px}
.field-label{position:absolute;top:-7px;left:12px;padding:0 5px;background:var(--white);color:var(--leaf);font-size:8.5px;font-weight:300}
.field--email{top:229px}
.field--password{top:283px}
.login-row{position:absolute;left:11px;right:11px;top:334px;display:flex;justify-content:space-between;font-size:8.5px;color:var(--muted);font-weight:300}
.login-row .check{display:inline-block;width:7px;height:7px;border:1px solid var(--muted);border-radius:1px;margin-right:5px;vertical-align:0}
.btn{position:absolute;left:11px;width:215px;height:31px;border-radius:16px;display:flex;align-items:center;justify-content:center;gap:6px;font-size:10.5px;font-weight:500}
.btn--lime{background:var(--lime);color:var(--ink)}
.btn--dark{background:var(--forest);color:var(--lime)}
.btn--login{top:364px}
.btn--start{top:361px}
.btn--send{top:401px}
.options-title{top:126px;font-size:17px}
.option{position:absolute;left:18px;width:201px;height:57px;border:1px solid var(--lime);border-radius:4px;background:var(--mint);padding:7px 0 0 72px}
.option h3{font-size:10px;font-weight:500;color:var(--ink);margin-bottom:3px}
.option p{font-size:7.8px;font-weight:300;line-height:13px;color:#111;padding-right:8px}
.option-icon{position:absolute;left:16px;top:10px;width:36px;height:36px}
.option--mobile{top:156px}
.option--cash{top:223px}
.option--bank{top:287px}
</style>
</head>
<body>
<main class="canvas">

  <section class="screen screen--splash" aria-label="Splash screen">
    <div class="splash-pattern" role="img" aria-label="Dark green background with a faint pattern of money and finance doodles"></div>
    <div class="brand brand--splash"><span class="brand-dot"></span>swiftsend</div>
    <div class="splash-strip"></div>
  </section>

  <section class="screen screen--welcome" aria-label="Welcome screen">
    <svg class="header" viewBox="0 0 237 130" aria-hidden="true">
      <defs><linearGradient id="dome1" x1="0" y1="0" x2="0" y2="1"><stop offset="0" stop-color="#1e6f1e"/><stop offset="1" stop-color="#74d24d"/></linearGradient></defs>
      <path d="M0 0H237V40C220 90 175 119 118 119C60 119 15 90 0 40Z" fill="url(#dome1)"/>
      <rect x="214" y="58" width="14" height="40" rx="7" transform="rotate(40 221 78)" fill="var(--lime)"/>
    </svg>
    <div class="status"><span>9:41 <small>AM</small></span><span class="status-icons">
      <svg width="10" height="8" viewBox="0 0 10 8"><path d="M1 3a6 6 0 0 1 8 0M2.5 4.6a3.6 3.6 0 0 1 5 0M5 7.5l1-1.2a1.4 1.4 0 0 0-2 0z" stroke="#fff" fill="#fff" stroke-width="1"/></svg>
      <svg width="9" height="8" viewBox="0 0 9 8" fill="#fff"><rect x="0" y="6" width="1.5" height="2"/><rect x="2.5" y="4" width="1.5" height="4"/><rect x="5" y="2" width="1.5" height="6"/><rect x="7.5" y="0" width="1.5" height="8"/></svg>
      <svg width="13" height="7" viewBox="0 0 13 7"><rect x=".5" y=".5" width="11" height="6" rx="1.2" fill="none" stroke="#fff"/><rect x="2" y="2" width="8" height="3" fill="#fff"/></svg></span></div>
    <div class="brand brand--header"><span class="brand-dot"></span>swiftsend</div>
    <h1 class="title welcome-title">Welcome to Swift Send</h1>
    <p class="welcome-sub">Sending money made Simple,<br>Fast &amp; Transparent</p>
    <p class="welcome-note"><span class="tick"></span>Send money online 24/7 when it's convenient for you</p>
    <div class="welcome-art" role="img" aria-label="Illustration of two hands holding phones with gold coins passing between them"></div>
  </section>

  <section class="screen screen--login" aria-label="Login screen">
    <svg class="header" viewBox="0 0 237 130" aria-hidden="true">
      <defs><linearGradient id="dome2" x1="0" y1="0" x2="0" y2="1"><stop offset="0" stop-color="#1e6f1e"/><stop offset="1" stop-color="#74d24d"/></linearGradient></defs>
      <path d="M0 0H237V40C220 85 172 107 118 107C62 107 15 85 0 40Z" fill="url(#dome2)"/>
      <rect x="214" y="58" width="14" height="40" rx="7" transform="rotate(40 221 78)" fill="var(--lime)"/>
    </svg>
    <div class="status"><span>9:41 <small>AM</small></span><span class="status-icons">
      <svg width="10" height="8" viewBox="0 0 10 8"><path d="M1 3a6 6 0 0 1 8 0M2.5 4.6a3.6 3.6 0 0 1 5 0M5 7.5l1-1.2a1.4 1.4 0 0 0-2 0z" stroke="#fff" fill="#fff" stroke-width="1"/></svg>
      <svg width="9" height="8" viewBox="0 0 9 8" fill="#fff"><rect x="0" y="6" width="1.5" height="2"/><rect x="2.5" y="4" width="1.5" height="4"/><rect x="5" y="2" width="1.5" height="6"/><rect x="7.5" y="0" width="1.5" height="8"/></svg>
      <svg width="13" height="7" viewBox="0 0 13 7"><rect x=".5" y=".5" width="11" height="6" rx="1.2" fill="none" stroke="#fff"/><rect x="2" y="2" width="8" height="3" fill="#fff"/></svg></span></div>
    <div class="brand brand--header"><span class="brand-dot"></span>swiftsend</div>
    <h1 class="title login-title">Login<br>to Your account</h1>
    <p class="login-hello">Hello, Welcome back to your account</p>
    <div class="field field--email"><span class="field-label">E-mail</span>example@email.com</div>
    <div class="field field--password"><span class="field-label">Password</span>your password</div>
    <div class="login-row"><span><span class="check"></span>Remember me</span><span>Forgot Password?</span></div>
    <div class="btn btn--lime btn--login">Login
      <svg width="13" height="13" viewBox="0 0 13 13"><circle cx="6.5" cy="6.5" r="6.5" fill="var(--ink)"/><circle cx="6.5" cy="5" r="2.2" fill="var(--lime)"/><path d="M2.6 10.5a4.4 3.4 0 0 1 7.8 0" fill="var(--lime)"/></svg></div>
  </section>

  <section class="screen screen--options" aria-label="More options to send screen">
    <svg class="header" viewBox="0 0 237 130" aria-hidden="true">
      <defs><linearGradient id="dome3" x1="0" y1="0" x2="0" y2="1"><stop offset="0" stop-color="#1e6f1e"/><stop offset="1" stop-color="#74d24d"/></linearGradient></defs>
      <path d="M0 0H237V40C220 85 172 107 118 107C62 107 15 85 0 40Z" fill="url(#dome3)"/>
      <rect x="214" y="58" width="14" height="40" rx="7" transform="rotate(40 221 78)" fill="var(--lime)"/>
    </svg>
    <div class="status"><span>9:41 <small>AM</small></span><span class="status-icons">
      <svg width="10" height="8" viewBox="0 0 10 8"><path d="M1 3a6 6 0 0 1 8 0M2.5 4.6a3.6 3.6 0 0 1 5 0M5 7.5l1-1.2a1.4 1.4 0 0 0-2 0z" stroke="#fff" fill="#fff" stroke-width="1"/></svg>
      <svg width="9" height="8" viewBox="0 0 9 8" fill="#fff"><rect x="0" y="6" width="1.5" height="2"/><rect x="2.5" y="4" width="1.5" height="4"/><rect x="5" y="2" width="1.5" height="6"/><rect x="7.5" y="0" width="1.5" height="8"/></svg>
      <svg width="13" height="7" viewBox="0 0 13 7"><rect x=".5" y=".5" width="11" height="6" rx="1.2" fill="none" stroke="#fff"/><rect x="2" y="2" width="8" height="3" fill="#fff"/></svg></span></div>
    <div class="brand brand--header"><span class="brand-dot"></span>swiftsend</div>
    <h1 class="title options-title">More options to send</h1>

    <article class="option option--mobile">
      <svg class="option-icon" viewBox="0 0 36 36" aria-hidden="true"><circle cx="18" cy="18" r="16" fill="none" stroke="var(--lime)" stroke-width="3" stroke-dasharray="18 7"/><rect x="13" y="9" width="10" height="18" rx="2" fill="var(--ink)"/><circle cx="20" cy="18" r="4" fill="var(--mint)" stroke="var(--ink)"/></svg>
      <h3>Mobile Money</h3><p>Realtime transfer to mobile wallet</p>
    </article>
    <article class="option option--cash">
      <svg class="option-icon" viewBox="0 0 36 36" aria-hidden="true"><circle cx="18" cy="18" r="16" fill="none" stroke="var(--lime)" stroke-width="3" stroke-dasharray="18 7"/><circle cx="18" cy="18" r="8" fill="none" stroke="var(--ink)" stroke-width="2"/><circle cx="18" cy="18" r="5" fill="var(--ink)"/></svg>
      <h3>Cash Pickup</h3><p>Pickup from our large network of agents</p>
    </article>
    <article class="option option--bank">
      <svg class="option-icon" viewBox="0 0 36 36" aria-hidden="true"><circle cx="18" cy="18" r="16" fill="none" stroke="var(--lime)" stroke-width="3" stroke-dasharray="18 7"/><path d="M10 16L18 11L26 16Z" fill="var(--ink)"/><rect x="11" y="17" width="2" height="7" fill="var(--ink)"/><rect x="17" y="17" width="2" height="7" fill="var(--ink)"/><rect x="23" y="17" width="2" height="7" fill="var(--ink)"/><rect x="10" y="25" width="16" height="2" fill="var(--ink)"/></svg>
      <h3>Bank Deposit</h3><p>Instant transfer to bank account</p>
    </article>

    <div class="btn btn--dark btn--start">Get Started
      <svg width="8" height="8" viewBox="0 0 8 8"><path d="M1 7L7 1M2.5 1H7V5.5" fill="none" stroke="var(--lime)" stroke-width="1.3"/></svg></div>
    <div class="btn btn--lime btn--send">Send Money
      <svg width="8" height="8" viewBox="0 0 8 8"><path d="M1 7L7 1M2.5 1H7V5.5" fill="none" stroke="var(--ink)" stroke-width="1.3"/></svg></div>
  </section>

</main>
</body>
</html>
```